Tervolan Pty Ltd professional business card

A professional business card template using the colours from the supplied logo.
Clean crisp lines while, Modern while not being over the top.

Target Market(s)

Construction, commerical and industrial

Industry/Entity Type

Communications

Contact Information for Business Card

For a Communications, IT, Optical fibre installation company

Colors
37b8a4

```html
<!DOCTYPE html>
<html lang="en">
<head>
<meta charset="utf-8">
<title>Tervolan Pty Ltd — Business Card</title>
<link rel="stylesheet" href="https://fonts.googleapis.com/css2?family=Montserrat:wght@500;700&display=swap">
<style>
  :root {
    --backdrop: #e4e4e4;
    --card-dark: #232323;
    --card-light: #4a4a4a;
    --brand-teal: #2399a3;
    --brand-grey: #6f6f74;
    --text-grey: #8a8a8e;
    --rule-grey: #8c8c8c;
  }
  * { box-sizing: border-box; margin: 0; padding: 0; }
  html, body {
    width: 1200px; height: 1200px; overflow: hidden;
    background: var(--backdrop);
    font-family: "Montserrat", Arial, sans-serif;
  }
  .card {
    position: absolute; left: 220px;
    width: 760px; height: 434px;
    background:
      radial-gradient(ellipse 420px 300px at 82% 18%, var(--card-light) 0%, rgba(74,74,74,0) 100%),
      var(--card-dark);
    overflow: hidden;
  }
  .card--front { top: 100px; }
  .card--back { top: 662px; }

  .wordmark {
    position: absolute; display: flex; align-items: center;
    color: var(--brand-grey); font-weight: 500; letter-spacing: 0.02em;
  }
  .wordmark__dot { border-radius: 50%; background: var(--brand-teal); flex: none; }
  .card--front .wordmark { right: 58px; top: 308px; font-size: 54px; gap: 14px; }
  .card--front .wordmark__dot { width: 22px; height: 22px; }
  .card--back .wordmark { left: 60px; top: 28px; font-size: 26px; gap: 8px; }
  .card--back .wordmark__dot { width: 12px; height: 12px; }

  .person { position: absolute; left: 60px; top: 208px; color: var(--brand-teal); }
  .person__name { font-size: 30px; font-weight: 700; letter-spacing: 0.04em; line-height: 1.1; }
  .person__role { font-size: 16px; font-weight: 500; letter-spacing: 0.03em; margin-top: 4px; }

  .contact {
    position: absolute; left: 60px; top: 280px; list-style: none;
    color: var(--text-grey); font-size: 16.5px; font-weight: 500; line-height: 25px;
    letter-spacing: 0.02em;
  }
  .card-lines { position: absolute; inset: 0; }
</style>
</head>
<body>
  <section class="card card--front" aria-label="Card front">
    <div class="wordmark"><span class="wordmark__dot"></span>TERVOLAN</div>
  </section>

  <section class="card card--back" aria-label="Card back">
    <div class="wordmark"><span class="wordmark__dot"></span>TERVOLAN</div>
    <div class="person">
      <h1 class="person__name">MAREN KALLOWAY</h1>
      <p class="person__role">DIRECTOR</p>
    </div>
    <ul class="contact">
      <li>+94 77 5550182</li>
      <li>admin@tervolan.com</li>
      <li>www.tervolan.com</li>
    </ul>
    <svg class="card-lines" width="760" height="434" viewBox="0 0 760 434" aria-hidden="true">
      <line x1="694" y1="0" x2="694" y2="434" stroke="var(--rule-grey)" stroke-width="1"/>
      <path d="M330 434 C 530 410 690 280 694 0" fill="none" stroke="var(--brand-teal)" stroke-width="1.3"/>
    </svg>
  </section>
</body>
</html>
```